Need Bold, Hip Card for Concert Ticket Website Gleaming Passes!

Hi there! I am putting together a business/website that sells event tickets (mostly concerts, but also some sports and theater). Think SeatNook, but much smaller. The site is called Gleaming Passes. I have a new logo (attached, with black/red/white color scheme), and am looking for a modern/cool/original business card design. Note that I am thinking of having the card itself in the shape of a ticket (die cut), so you may want to keep that in mind when designing, but I'm not set on that. I'm also open to alternative card sizes, thicknesses, glossy, spot UV, etc. in order to stand out. I'm attaching a potential die cut template and a sample card using that template in case you want to work with that.
Target Market(s)
Music fans, people that like going to see live events
Industry/Entity Type
Entertainment
Contact Information for Business Card
Information that I'd like to have:
website address - www.gleamingpasses.example
phone number: 1-833-5GLEAMNG (532-6264)
my name - Wendel Pike

```html
<!DOCTYPE html>
<html lang="en">
<head>
<meta charset="utf-8">
<title>Gleaming Passes — Business Card</title>
<link rel="stylesheet" href="https://fonts.googleapis.com/css2?family=Oswald:wght@500;700&display=swap">
<style>
  :root {
    --stage: #e2e2e2;
    --paper: #f3ecd9;
    --paper-edge: #e6dcc2;
    --ticket-red: #d0161c;
    --brand-red: #9e1b20;
    --ink: #1b1b1b;
  }
  html, body {
    margin: 0;
    padding: 0;
    width: 1200px;
    height: 1100px;
    overflow: hidden;
    background: var(--stage);
  }
  .sheet {
    position: relative;
    width: 1200px;
    height: 1100px;
  }
  .ticket {
    position: absolute;
    left: 170px;
    width: 860px;
    height: 472px;
    filter: drop-shadow(0 8px 14px rgba(0,0,0,0.28));
  }
  .ticket--front { top: 50px; }
  .ticket--back  { top: 578px; }
  .ticket__paper { fill: var(--paper); stroke: var(--paper-edge); stroke-width: 0.6; }
  .ticket__frame { fill: none; stroke: var(--ticket-red); stroke-width: 2.6; }
  .ticket__star  { fill: var(--brand-red); }
  .brand-name {
    font-family: "Oswald", sans-serif;
    font-weight: 700;
    fill: var(--brand-red);
  }
  .stub-url, .contact {
    font-family: "Oswald", sans-serif;
    font-weight: 700;
    fill: var(--ticket-red);
  }
  .contact--name { font-weight: 500; }
  .divider-wave { fill: none; stroke: var(--ink); stroke-width: 1.3; }
  .stub-digits {
    font-family: "Oswald", sans-serif;
    font-weight: 500;
    fill: var(--ink);
    letter-spacing: 1.6px;
  }
  .phone-icon { fill: var(--ink); }
</style>
</head>
<body>
<main class="sheet">

  <!-- Front of card -->
  <svg class="ticket ticket--front" viewBox="0 0 410 225" role="group" aria-label="Gleaming Passes ticket card, front">
    <defs>
      <path id="star" d="M0,-5.6 L1.32,-1.81 L5.33,-1.74 L2.13,0.69 L3.29,4.54 L0,2.24 L-3.29,4.54 L-2.13,0.69 L-5.33,-1.74 L-1.32,-1.81 Z"/>
      <path id="ticket-shape" d="M18,0 H392 A18,18 0 0 0 410,18 V207 A18,18 0 0 0 392,225 H18 A18,18 0 0 0 0,207 V18 A18,18 0 0 0 18,0 Z"/>
    </defs>
    <use href="#ticket-shape" class="ticket__paper"/>
    <rect class="ticket__frame" x="34" y="22" width="344" height="181" rx="14"/>
    <line class="ticket__frame" x1="334" y1="22" x2="334" y2="203"/>

    <g class="ticket__star">
      <use href="#star" x="70" y="44"/><use href="#star" x="99" y="44"/><use href="#star" x="128" y="44"/>
      <use href="#star" x="157" y="44"/><use href="#star" x="186" y="44"/><use href="#star" x="215" y="44"/>
      <use href="#star" x="244" y="44"/><use href="#star" x="273" y="44"/><use href="#star" x="302" y="44"/>
      <use href="#star" x="70" y="183"/><use href="#star" x="99" y="183"/><use href="#star" x="128" y="183"/>
      <use href="#star" x="157" y="183"/><use href="#star" x="186" y="183"/><use href="#star" x="215" y="183"/>
      <use href="#star" x="244" y="183"/><use href="#star" x="273" y="183"/><use href="#star" x="302" y="183"/>
    </g>

    <text class="brand-name" x="184" y="124" text-anchor="middle" font-size="32">Gleaming Passes</text>

    <text class="stub-url" transform="translate(362 112.5) rotate(-90)" text-anchor="middle" font-size="12.5" textLength="168" lengthAdjust="spacingAndGlyphs">www.gleamingpasses.example</text>
  </svg>

  <!-- Back of card -->
  <svg class="ticket ticket--back" viewBox="0 0 410 225" role="group" aria-label="Gleaming Passes ticket card, back with contact details">
    <use href="#ticket-shape" class="ticket__paper"/>
    <rect class="ticket__frame" x="40" y="22" width="306" height="181" rx="14"/>
    <line class="ticket__frame" x1="298" y1="22" x2="298" y2="203"/>

    <g class="ticket__star">
      <use href="#star" x="22" y="82"/><use href="#star" x="22" y="100"/><use href="#star" x="22" y="118"/>
      <use href="#star" x="22" y="136"/><use href="#star" x="22" y="154"/>
    </g>

    <text class="contact contact--name" x="169" y="60" text-anchor="middle" font-size="22">Wendel Pike</text>
    <path class="divider-wave" d="M123,72 q4,-3 8,0 t8,0 t8,0 t8,0 t8,0 t8,0 t8,0 t8,0 t8,0 t8,0 t8,0 t8,0"/>
    <text class="contact" x="169" y="106" text-anchor="middle" font-size="17">1-833-5GLEAMNG</text>
    <text class="contact" x="169" y="129" text-anchor="middle" font-size="17">(532-6264)</text>
    <path class="divider-wave" d="M123,142 q4,-3 8,0 t8,0 t8,0 t8,0 t8,0 t8,0 t8,0 t8,0 t8,0 t8,0 t8,0 t8,0"/>
    <text class="contact" x="169" y="178" text-anchor="middle" font-size="14" textLength="238" lengthAdjust="spacingAndGlyphs">www.gleamingpasses.example</text>

    <text class="brand-name" transform="translate(326 112.5) rotate(-90)" text-anchor="middle" font-size="13">Gleaming Passes</text>

    <text class="stub-digits" transform="translate(369 108) rotate(-90)" text-anchor="middle" font-size="10">18335326264</text>
    <g class="phone-icon" transform="translate(364.5 176)">
      <rect x="0" y="0" width="9" height="8" rx="1.4"/>
      <rect x="-1" y="-2" width="11" height="2.4" rx="1.2"/>
    </g>
  </svg>

</main>
</body>
</html>
```